Brownie Snack Packaging

Design the film wrapper packaging for a brownie snack. It needs to be cohesive with our existing product line (please review attached photos), but still differentiated from it to avoid customer confusion.
Brief is outlined in the images attached. Please review prior to submitting designs. All designs should have the iridescent white pearl packaging color, with the text:
High Protein Brownie
10g Protein
Vegan
Gluten-Free
No Added Sugars
We would like to see designs with square packaging with a mouth-watering brownie image being the most prominent. Logo of brand "ORUNE" should be in upper right corner.
Note: we have another product line of cashew butter sachets that are pink, blue, & chocolate - I'm attaching those for reference so you can design these brownies to look somewhat related to the cashew butters.
Look and feel
Each slider illustrates characteristics of the customer's brand and the style your logo design should communicate.

```html
<!DOCTYPE html>
<html lang="en">
<head>
<meta charset="utf-8">
<title>ORUNE High Protein Brownie – Wrapper Designs</title>
<link href="https://fonts.googleapis.com/css2?family=Josefin+Sans:wght@300&family=Montserrat:wght@400;600&family=Vollkorn:wght@700&display=swap" rel="stylesheet">
<style>
  :root {
    --paper: #ffffff;
    --ink-dark: #3b1d14;
    --ink-mid: #5e4638;
    --ink-soft: #4a3a33;
    --logo-gold: #8a6f47;
    --rule: #7a6a62;
    --pearl-lilac: #b9b4e2;
    --pearl-cyan: #c4ecf4;
    --pearl-pink: #f3c9df;
    --pearl-butter: #f6edc4;
    --pearl-white: #f4f2fb;
    --brownie-deep: #3a2016;
    --brownie-mid: #6b3f2a;
  }
  html, body {
    margin: 0;
    padding: 0;
    width: 1200px;
    height: 1200px;
    overflow: hidden;
    background: var(--paper);
  }
  .sheet {
    position: relative;
    width: 1200px;
    height: 1200px;
  }
  .wrapper {
    position: absolute;
    display: block;
  }
  .wrapper--classic { left: 90px; top: 300px; width: 450px; }
  .wrapper--bold { left: 660px; top: 270px; width: 450px; }
  .logo-name {
    font-family: "Josefin Sans", sans-serif;
    font-weight: 300;
    fill: var(--logo-gold);
  }
  .headline {
    font-family: "Vollkorn", serif;
    font-weight: 700;
  }
  .headline--classic { fill: var(--ink-dark); font-size: 28px; letter-spacing: 1px; }
  .headline--bold { fill: var(--ink-mid); font-size: 58px; letter-spacing: 1px; }
  .protein {
    font-family: "Montserrat", sans-serif;
    font-weight: 600;
  }
  .protein--classic { fill: var(--ink-dark); font-size: 22px; }
  .protein--bold { fill: var(--ink-mid); font-size: 22px; }
  .claim {
    font-family: "Montserrat", sans-serif;
    font-weight: 400;
    fill: var(--ink-soft);
  }
  .claim--classic { font-size: 18px; }
  .claim--bold { font-size: 20px; }
  .claim-rule { stroke: var(--rule); stroke-width: 1.5; }
  .swatch {
    position: absolute;
    left: 74px;
    top: 1096px;
    width: 124px;
    height: 74px;
  }
  .swatch-label {
    position: absolute;
    left: 247px;
    top: 1118px;
    margin: 0;
    font-family: "Montserrat", sans-serif;
    font-weight: 400;
    font-size: 30px;
    line-height: 1;
    color: #000;
  }
</style>
</head>
<body>
<main class="sheet">

  <svg class="wrapper wrapper--classic" viewBox="0 0 496 514" aria-label="Wrapper design, classic layout">
    <defs>
      <linearGradient id="pearlBase" x1="0" y1="0" x2="1" y2="1">
        <stop offset="0" stop-color="var(--pearl-lilac)"/>
        <stop offset="0.45" stop-color="var(--pearl-cyan)"/>
        <stop offset="0.7" stop-color="var(--pearl-pink)"/>
        <stop offset="1" stop-color="var(--pearl-white)"/>
      </linearGradient>
      <radialGradient id="pearlGlow" cx="0.8" cy="0.1" r="0.5">
        <stop offset="0" stop-color="var(--pearl-butter)" stop-opacity="0.9"/>
        <stop offset="1" stop-color="var(--pearl-butter)" stop-opacity="0"/>
      </radialGradient>
      <radialGradient id="pearlRainbow" cx="0.15" cy="0.72" r="0.35">
        <stop offset="0" stop-color="var(--pearl-pink)"/>
        <stop offset="0.5" stop-color="var(--pearl-butter)" stop-opacity="0.7"/>
        <stop offset="1" stop-color="var(--pearl-cyan)" stop-opacity="0"/>
      </radialGradient>
      <radialGradient id="brownieTone" cx="0.5" cy="0.5" r="0.5">
        <stop offset="0" stop-color="var(--brownie-mid)"/>
        <stop offset="0.6" stop-color="var(--brownie-deep)"/>
        <stop offset="1" stop-color="var(--brownie-deep)" stop-opacity="0"/>
      </radialGradient>
    </defs>
    <rect class="wrapper-base" width="496" height="514" fill="var(--paper)"/>
    <polygon class="pearl-field" points="0,0 496,0 496,238 0,514" fill="url(#pearlBase)"/>
    <polygon class="pearl-field" points="0,0 496,0 496,238 0,514" fill="url(#pearlGlow)"/>
    <polygon class="pearl-field" points="0,0 496,0 496,238 0,514" fill="url(#pearlRainbow)"/>
    <text class="logo-name" x="445" y="88" text-anchor="end" font-size="66">ORUNE</text>
    <ellipse class="brownie-photo" role="img" aria-label="Photo of a chocolate brownie bar drizzled with chocolate sauce" cx="250" cy="250" rx="220" ry="135" fill="url(#brownieTone)"/>
    <text class="headline headline--classic" x="28" y="408">HIGH  PROTEIN</text>
    <text class="headline headline--classic" x="28" y="443">BROWNIE</text>
    <text class="protein protein--classic" x="312" y="406">10g protein</text>
    <text class="claim claim--classic" x="30" y="494">Gluten-Free</text>
    <line class="claim-rule" x1="163" y1="466" x2="163" y2="504"/>
    <text class="claim claim--classic" x="188" y="494">Vegan</text>
    <line class="claim-rule" x1="266" y1="466" x2="266" y2="504"/>
    <text class="claim claim--classic" x="283" y="494">No Added Sugars</text>
  </svg>

  <svg class="wrapper wrapper--bold" viewBox="0 0 507 589" aria-label="Wrapper design, bold headline layout">
    <defs>
      <linearGradient id="pearlBase2" x1="0" y1="0" x2="1" y2="1">
        <stop offset="0" stop-color="var(--pearl-lilac)"/>
        <stop offset="0.4" stop-color="var(--pearl-cyan)"/>
        <stop offset="0.65" stop-color="var(--pearl-pink)"/>
        <stop offset="1" stop-color="var(--pearl-white)"/>
      </linearGradient>
      <radialGradient id="pearlGlow2" cx="0.85" cy="0.05" r="0.45">
        <stop offset="0" stop-color="var(--pearl-butter)" stop-opacity="0.9"/>
        <stop offset="1" stop-color="var(--pearl-butter)" stop-opacity="0"/>
      </radialGradient>
      <radialGradient id="pearlRainbow2" cx="0.2" cy="0.5" r="0.35">
        <stop offset="0" stop-color="var(--pearl-pink)"/>
        <stop offset="0.5" stop-color="var(--pearl-butter)" stop-opacity="0.7"/>
        <stop offset="1" stop-color="var(--pearl-cyan)" stop-opacity="0"/>
      </radialGradient>
      <radialGradient id="brownieTone2" cx="0.5" cy="0.5" r="0.5">
        <stop offset="0" stop-color="var(--brownie-mid)"/>
        <stop offset="0.6" stop-color="var(--brownie-deep)"/>
        <stop offset="1" stop-color="var(--brownie-deep)" stop-opacity="0"/>
      </radialGradient>
    </defs>
    <rect class="wrapper-base" width="507" height="589" fill="var(--paper)"/>
    <polygon class="pearl-field" points="0,0 507,0 507,270 0,589" fill="url(#pearlBase2)"/>
    <polygon class="pearl-field" points="0,0 507,0 507,270 0,589" fill="url(#pearlGlow2)"/>
    <polygon class="pearl-field" points="0,0 507,0 507,270 0,589" fill="url(#pearlRainbow2)"/>
    <ellipse class="brownie-photo" role="img" aria-label="Photo of a chocolate brownie bar drizzled with chocolate sauce" cx="210" cy="185" rx="180" ry="110" fill="url(#brownieTone2)"/>
    <text class="logo-name" transform="translate(405 40) rotate(90)" font-size="72">ORUNE</text>
    <text class="headline headline--bold" x="262" y="392" text-anchor="middle">HIGH  PROTEIN</text>
    <text class="headline headline--bold" x="262" y="462" text-anchor="middle">BROWNIE</text>
    <text class="protein protein--bold" x="251" y="520" text-anchor="middle">10g protein</text>
    <text class="claim claim--bold" x="66" y="570">Gluten-Free</text>
    <line class="claim-rule" x1="200" y1="536" x2="200" y2="580"/>
    <text class="claim claim--bold" x="220" y="570">Vegan</text>
    <line class="claim-rule" x1="303" y1="536" x2="303" y2="580"/>
    <text class="claim claim--bold" x="318" y="570">No Added Sugars</text>
  </svg>

  <svg class="swatch" viewBox="0 0 124 74" role="img" aria-label="Iridescent pearl colour swatch">
    <defs>
      <linearGradient id="swatchTone" x1="0" y1="0" x2="1" y2="1">
        <stop offset="0" stop-color="var(--pearl-lilac)"/>
        <stop offset="0.45" stop-color="var(--pearl-white)"/>
        <stop offset="0.6" stop-color="var(--pearl-pink)"/>
        <stop offset="0.8" stop-color="var(--pearl-cyan)"/>
        <stop offset="1" stop-color="var(--pearl-lilac)"/>
      </linearGradient>
    </defs>
    <rect width="124" height="74" fill="url(#swatchTone)"/>
  </svg>
  <p class="swatch-label">iridescent</p>

</main>
</body>
</html>
```